CopperNomad Stretching and Strength

We need a application design for a our first IOS application. the goal of the application is to categorize stretching and strength routines for triathlon.

We would like to see designs that use the color orange.

The design of the application should be compliant with the last version of the IOS Mobile.

For this first design we need the folowing pages:

1- Sign up
2- Log in
3- Home
4- View Exercises
5- Do it
6- Profile

The description of each page is in the attached document.

We need a logo design for the application. The logo should express that mission of the application that is for stretch and strength training for Triathlon.

We will use https://plinthkit.example to develop the application, if you have any experience of the limitation that this technology have it will be a plus.

If you have any question please feel free to contact us.
Updates

Project Deadline Extended
Reason: We will extend the deadline to be sure that we select the best design from all of you. we will take the final decision next Tuesday.

Target Market(s)

The market for my aplicación is the Running a Triathlon world.

Logo Text

CopperNomad

Font styles to use
Serif

Colors
f37122
ffffff
dcdcdc

Requirements
Must have
• In some future we will add more features in the menu. We should considere it for the design.
• The designs should include all the screens in the power point.

```html
<!DOCTYPE html>
<html lang="en">
<head>
<meta charset="utf-8">
<title>CopperNomad – Sign Up</title>
<link href="https://fonts.googleapis.com/css2?family=Roboto:ital,wght@0,400;0,500;0,700;1,400&display=swap" rel="stylesheet">
<style>
  :root {
    --orange: #f37122;
    --white: #ffffff;
    --field-bg: #ffffff;
    --screen-bg: #e9edf1;
    --page-bg: #d6e4f0;
    --text: #555b60;
    --text-dark: #3d4246;
    --icon: #7c7f82;
    --avatar: #d6d6d6;
    --social-blue: #1b5fb5;
    --chip: #dcdcdc;
  }
  * { box-sizing: border-box; margin: 0; padding: 0; }
  html, body {
    width: 1200px; height: 1200px; overflow: hidden;
    background: var(--page-bg);
    font-family: 'Roboto', Arial, sans-serif;
  }
  .screen {
    position: absolute; left: 275px; top: 20px;
    width: 550px; height: 982px;
    transform: scale(1.18); transform-origin: top left;
    background: var(--screen-bg);
    overflow: hidden;
  }
  .status-bar {
    position: absolute; left: 0; top: 0; width: 100%; height: 40px;
    background: var(--orange); color: var(--white);
    font-size: 16px;
  }
  .status-bar .carrier { position: absolute; left: 7px; top: 11px; display: flex; align-items: center; gap: 6px; }
  .status-bar .time { position: absolute; left: 0; right: 0; top: 11px; text-align: center; }
  .status-bar .power { position: absolute; right: 8px; top: 11px; display: flex; align-items: center; gap: 6px; }
  .back-button { position: absolute; left: 12px; top: 60px; }
  .avatar {
    position: absolute; left: 212px; top: 78px; width: 124px; height: 124px;
    border-radius: 50%; background: var(--avatar);
    border: 4px solid var(--white);
    box-shadow: 0 0 0 1px #d0d4d8;
  }
  .avatar-label {
    position: absolute; left: 0; right: 0; top: 216px; text-align: center;
    font-size: 14px; font-weight: 500; color: var(--text-dark); letter-spacing: 0.2px;
  }
  .field {
    position: absolute; left: 37px; width: 476px; height: 56px;
    background: var(--field-bg);
    box-shadow: 0 1px 2px rgba(0,0,0,0.12);
    display: flex; align-items: center; justify-content: space-between;
    padding: 0 20px 0 21px;
    font-size: 19px; color: var(--text);
  }
  .field svg { flex: none; }
  .field.half { width: 233px; }
  .field.gender { left: 280px; }
  .consent { position: absolute; left: 37px; top: 687px; display: flex; align-items: center; gap: 13px; font-size: 17px; color: var(--text); }
  .checkbox { width: 21px; height: 21px; border: 1.5px solid var(--orange); background: var(--white); display: flex; align-items: center; justify-content: center; }
  .create-button {
    position: absolute; left: 37px; top: 743px; width: 476px; height: 61px;
    border-radius: 31px; background: var(--orange);
    box-shadow: 0 2px 3px rgba(0,0,0,0.15);
    color: var(--white); font-size: 21px; font-weight: 700;
    display: flex; align-items: center; justify-content: center;
  }
  .login-prompt { position: absolute; left: 0; right: 0; top: 826px; text-align: center; font-size: 17px; color: var(--text); }
  .login-prompt .link { color: var(--orange); text-decoration: underline; font-weight: 500; }
  .divider-or {
    position: absolute; left: 263px; top: 864px; width: 24px; height: 24px; border-radius: 50%;
    background: var(--chip); font-size: 12px; color: var(--text-dark);
    display: flex; align-items: center; justify-content: center;
  }
  .social-bar { position: absolute; left: 0; top: 916px; width: 100%; height: 66px; display: flex; }
  .social { flex: 1; display: flex; align-items: center; font-size: 20px; white-space: nowrap; }
  .social em { font-size: 17px; }
  .social .dot { width: 40px; height: 40px; border-radius: 50%; flex: none; }
  .social.linkora { background: var(--social-blue); color: var(--white); padding-left: 12px; gap: 14px; }
  .social.linkora .dot { background: var(--white); }
  .social.postvale { background: var(--white); color: var(--text-dark); padding-left: 30px; gap: 14px; }
  .social.postvale .dot { background: #eeeeee; }
</style>
</head>
<body>
  <main class="screen">
    <header class="status-bar">
      <div class="carrier">
        <svg width="48" height="10" viewBox="0 0 48 10"><g fill="#fff" stroke="#fff"><circle cx="5" cy="5" r="4"/><circle cx="15" cy="5" r="4"/><circle cx="25" cy="5" r="4"/><circle cx="35" cy="5" r="3.5" fill="none"/><circle cx="44" cy="5" r="3.5" fill="none"/></g></svg>
        <span>KESTRA</span>
        <svg width="16" height="12" viewBox="0 0 16 12"><path d="M1 4a10 10 0 0 1 14 0M3.5 6.5a6.5 6.5 0 0 1 9 0M6 9a3 3 0 0 1 4 0" fill="none" stroke="#fff" stroke-width="1.8"/><circle cx="8" cy="11" r="1" fill="#fff"/></svg>
      </div>
      <div class="time">4:21 PM</div>
      <div class="power">
        <span>100%</span>
        <svg width="36" height="14" viewBox="0 0 36 14"><rect x="0.5" y="0.5" width="31" height="13" rx="3" fill="none" stroke="#fff"/><rect x="2" y="2" width="28" height="10" rx="2" fill="#fff"/><rect x="33" y="4.5" width="2" height="5" rx="1" fill="#fff"/></svg>
      </div>
    </header>

    <svg class="back-button" width="26" height="18" viewBox="0 0 26 18"><path d="M25 9H2M9 2L2 9l7 7" fill="none" stroke="#555" stroke-width="1.6"/></svg>

    <div class="avatar" role="img" aria-label="Profile photo placeholder"></div>
    <div class="avatar-label">ADD YOUR PHOTO</div>

    <div class="field" style="top:273px"><span>Full Name</span>
      <svg width="18" height="22" viewBox="0 0 18 22"><circle cx="9" cy="6" r="5" fill="var(--icon)"/><path d="M0 22v-4c0-4 4-6 9-6s9 2 9 6v4z" fill="var(--icon)"/></svg></div>
    <div class="field" style="top:339px"><span>Email Id</span>
      <svg width="21" height="16" viewBox="0 0 21 16"><rect width="21" height="16" rx="1.5" fill="var(--icon)"/><path d="M1 2l9.5 7L20 2" fill="none" stroke="#fff" stroke-width="1.6"/></svg></div>
    <div class="field half" style="top:405px"><span>Age</span>
      <svg width="22" height="22" viewBox="0 0 22 22"><rect x="1" y="3" width="20" height="18" fill="none" stroke="var(--icon)" stroke-width="2"/><rect x="1" y="3" width="20" height="5" fill="var(--icon)"/><path d="M6 1v4M16 1v4" stroke="var(--icon)" stroke-width="2"/><g fill="var(--icon)"><rect x="5" y="11" width="3" height="3"/><rect x="9.5" y="11" width="3" height="3"/><rect x="14" y="11" width="3" height="3"/><rect x="5" y="15.5" width="3" height="3"/><rect x="9.5" y="15.5" width="3" height="3"/><rect x="14" y="15.5" width="3" height="3"/></g></svg></div>
    <div class="field half gender" style="top:405px"><span>Gender:</span>
      <svg width="16" height="9" viewBox="0 0 16 9"><path d="M0 0h16L8 9z" fill="var(--icon)"/></svg></div>
    <div class="field" style="top:471px"><span>Sport:</span>
      <svg width="16" height="9" viewBox="0 0 16 9"><path d="M0 0h16L8 9z" fill="var(--icon)"/></svg></div>
    <div class="field" style="top:537px"><span>User Name</span>
      <svg width="18" height="22" viewBox="0 0 18 22"><circle cx="9" cy="6" r="5" fill="var(--icon)"/><path d="M0 22v-4c0-4 4-6 9-6s9 2 9 6v4z" fill="var(--icon)"/></svg></div>
    <div class="field" style="top:603px"><span>Password</span>
      <svg width="18" height="22" viewBox="0 0 18 22"><path d="M4 10V6a5 5 0 0 1 10 0v4" fill="none" stroke="var(--icon)" stroke-width="2.4"/><rect x="1" y="9" width="16" height="13" rx="1.5" fill="var(--icon)"/><rect x="8" y="13" width="2" height="5" fill="#fff"/></svg></div>

    <label class="consent">
      <span class="checkbox"><svg width="13" height="10" viewBox="0 0 13 10"><path d="M1 5l4 4 7-8" fill="none" stroke="var(--orange)" stroke-width="1.5"/></svg></span>
      <span>Receive Email</span>
    </label>

    <div class="create-button">CREATE ACCOUNT</div>

    <p class="login-prompt">You already have an account? <span class="link">LOG IN</span> now</p>
    <div class="divider-or">OR</div>

    <nav class="social-bar">
      <div class="social linkora"><span class="dot"></span><span>Sign up <em>with</em> Linkora</span></div>
      <div class="social postvale"><span class="dot"></span><span>Sign up <em>with</em> Postvale</span></div>
    </nav>
  </main>
</body>
</html>
```